Brightwater Health Partners, LLC Business Card update!

would like a classier business card. Our cards currently just have our logo and contact information. Need better use of color and creativity
Logo attached.

Target Market(s)

Potential clients, contacts, existing clients. We are a consulting company

Industry/Entity Type

Business

Contact Information for Business Card

We like our colors but just have a boring card with our logo and a white background. I want something that stands out.

Colors
ec1f27
757575

Requirements
Must have
• Color to stay consistent. Logo provided
Nice to have
• Just better use of color/ design

```html
<!DOCTYPE html>
<html lang="en">
<head>
<meta charset="utf-8">
<title>Brightwater Health Partners – Business Card</title>
<link rel="stylesheet" href="https://fonts.googleapis.com/css2?family=Exo+2:wght@400;500;600&display=swap">
<style>
  :root {
    --brand-red: #ec1f27;
    --brand-grey: #757575;
    --ink: #333333;
    --paper: #ffffff;
    --paper-shade: #ececec;
    --backdrop: #e4e4e6;
  }
  * { margin: 0; padding: 0; box-sizing: border-box; }
  html, body { width: 1200px; height: 899px; overflow: hidden; }
  body {
    background: var(--backdrop);
    font-family: "Exo 2", sans-serif;
    display: flex;
    align-items: center;
    justify-content: center;
    gap: 40px;
  }
  .card {
    position: relative;
    width: 540px;
    height: 309px;
    background: radial-gradient(ellipse at 40% 40%, var(--paper) 0%, var(--paper) 45%, var(--paper-shade) 100%);
    box-shadow: 0 6px 18px rgba(0,0,0,0.18);
    overflow: hidden;
  }
  .card-art { position: absolute; inset: 0; }
  .company-name {
    color: var(--brand-red);
    font-weight: 500;
    line-height: 1.05;
  }
  /* back */
  .card-back { display: flex; align-items: center; justify-content: center; }
  .card-back .company-name { font-size: 30px; text-align: center; }
  /* front */
  .card-front .company-name {
    position: absolute;
    left: 34px;
    top: 96px;
    font-size: 26px;
  }
  .holder {
    position: absolute;
    right: 22px;
    top: 56px;
    text-align: right;
    color: var(--paper);
  }
  .holder-name { font-size: 19px; font-weight: 600; letter-spacing: 1.5px; }
  .holder-role { font-size: 13px; font-weight: 500; letter-spacing: 0.6px; margin-top: 4px; }
  .contacts {
    position: absolute;
    left: 30px;
    top: 184px;
    list-style: none;
    color: var(--ink);
    font-size: 11.5px;
    letter-spacing: 0.6px;
  }
  .contacts li { display: flex; align-items: center; gap: 8px; height: 20px; }
  .contacts svg { width: 12px; height: 12px; fill: var(--ink); flex: none; }
  .address {
    position: absolute;
    right: 86px;
    bottom: 18px;
    color: var(--ink);
    font-size: 12px;
    line-height: 1.45;
    letter-spacing: 0.6px;
    text-align: left;
  }
</style>
</head>
<body>

  <section class="card card-back" aria-label="Business card, back">
    <p class="company-name">Brightwater<br>Health Partners</p>
  </section>

  <section class="card card-front" aria-label="Business card, front">
    <svg class="card-art" viewBox="0 0 540 309" preserveAspectRatio="none" aria-hidden="true">
      <path d="M0,0 H540 V232 C500,118 300,36 0,34 Z" fill="var(--brand-red)"/>
      <path d="M0,40 C300,42 500,124 540,242 V300 C500,146 300,48 0,44 Z" fill="var(--brand-grey)"/>
    </svg>

    <div class="holder">
      <p class="holder-name">DANIEL WHITFORD</p>
      <p class="holder-role">Managing Director</p>
    </div>

    <p class="company-name">Brightwater<br>Health Partners</p>

    <ul class="contacts">
      <li><svg viewBox="0 0 24 24"><path d="M6.6 10.8a15.1 15.1 0 0 0 6.6 6.6l2.2-2.2c.3-.3.7-.4 1-.2 1.1.4 2.3.6 3.6.6.6 0 1 .4 1 1V20c0 .6-.4 1-1 1A17 17 0 0 1 3 4c0-.6.4-1 1-1h3.5c.6 0 1 .4 1 1 0 1.3.2 2.5.6 3.6.1.3 0 .7-.2 1z"/></svg>014 562 7830</li>
      <li><svg viewBox="0 0 24 24"><path d="M7 1h10a2 2 0 0 1 2 2v18a2 2 0 0 1-2 2H7a2 2 0 0 1-2-2V3a2 2 0 0 1 2-2zm0 3v14h10V4zm5 15.5a1.2 1.2 0 1 0 0 2.4 1.2 1.2 0 0 0 0-2.4z"/></svg>014 562 7830</li>
      <li><svg viewBox="0 0 24 24"><path d="M6 2h10v6H6zM3 9h18v11H3zm3 3v2h2v-2zm4 0v2h2v-2zm4 0v2h2v-2zm-8 4v2h2v-2zm4 0v2h2v-2z"/></svg>014 562 7830</li>
      <li><svg viewBox="0 0 24 24"><path d="M2 5h20v14H2zm2 2v.5l8 5 8-5V7zm0 3v7h16v-7l-8 5z"/></svg>hello@brightwaterhp.com</li>
      <li><svg viewBox="0 0 24 24"><path d="M12 2a10 10 0 1 0 0 20 10 10 0 0 0 0-20zm6.9 6h-2.9a15 15 0 0 0-1.4-3.9A8 8 0 0 1 18.9 8zM12 4c.8 1.2 1.5 2.5 1.9 4h-3.8c.4-1.5 1.1-2.8 1.9-4zM4.3 14a8 8 0 0 1 0-4h3.4a16 16 0 0 0 0 4zm.8 2H8a15 15 0 0 0 1.4 3.9A8 8 0 0 1 5.1 16zM8 8H5.1a8 8 0 0 1 4.3-3.9A15 15 0 0 0 8 8zm4 12c-.8-1.2-1.5-2.5-1.9-4h3.8c-.4 1.5-1.1 2.8-1.9 4zm2.3-6H9.7a14 14 0 0 1 0-4h4.6a14 14 0 0 1 0 4zm.3 5.9A15 15 0 0 0 16 16h2.9a8 8 0 0 1-4.3 3.9zM16.3 14a16 16 0 0 0 0-4h3.4a8 8 0 0 1 0 4z"/></svg>www.brightwaterhp.com</li>
    </ul>

    <p class="address">27, 9th Floor,<br>Harbor Point Road</p>
  </section>

</body>
</html>
```